New CRM Software Needs an Awesome Banner Ad Campaign Design

Design of digital ads for sizes needed for LinkedIn and Google Remarketing.

Same design will be needed in various sizes (see attached word document for details and instructions).

We need an ad set design promoting a new cloud-based CRM (Customer Relationship Management) software. https://www.brightledgerhub.example/
We are looking for eye-catching, WOW designs, something attractive, but keep it professional. It should also convey quality, security and trust.
Updates

Project Deadline Extended Reason: I am extending the deadline in hopes to get more designers to submit. You need only to submit your design concept in one size. If I choose your design, then you can make the rest of the sizes.Thank you to all who have already submitted! Added Monday, January 16, 2017

Target Market(s)

B2B Audience –Mortgage and bank industries

Industry/Entity Type

Business Software

Font styles to use
Other font styles liked:
• Universe Condensed

Requirements
Must have
• Only one design concept in one size is needed initially, once you are awarded with the project, you can make the other sizes as specified and required.
• Please see attached word document for details and instructions.
• Must have both logos attached as well as use our colors and a modern image appealing to mortgage and banking executives.
Nice to have
Should not have
• Should not have a whole bunch of words and no pictures.

```html
<!DOCTYPE html>
<html lang="en">
<head>
<meta charset="utf-8">
<title>BrightLedgerHub – CRM for Mortgage Ad Set</title>
<link rel="stylesheet" href="https://fonts.googleapis.com/css2?family=Arimo:wght@400;700&display=swap">
<style>
  :root {
    --maroon: #6b2236;
    --maroon-dark: #4f1626;
    --steel: #5e7f9c;
    --steel-light: #9fb6c9;
    --gold: #d8c69c;
    --orange-top: #ffb23c;
    --orange-bottom: #e2650c;
    --button-ink: #4a1a0a;
    --play-disc: #5a1c10;
    --brand: #4d6d8c;
    --white: #ffffff;
    --label: #111111;
    --photo-a: #c9b8a6;
    --photo-b: #6f6a62;
    --photo-c: #e9e4dc;
  }
  * { box-sizing: border-box; margin: 0; padding: 0; }
  html, body { width: 1200px; height: 1200px; overflow: hidden; background: var(--white); }
  body { position: relative; font-family: "Arimo", Arial, sans-serif; }

  .banner { position: absolute; background: var(--white); border: 1px solid #9a9a9a; overflow: hidden; }
  .banner svg.shapes { position: absolute; inset: 0; }
  .size-label { position: absolute; font-size: 20px; color: var(--label); text-align: center; width: 200px; }

  .photo {
    position: absolute;
    background: linear-gradient(135deg, var(--photo-c) 0%, var(--photo-a) 45%, var(--photo-b) 100%);
  }

  .brand { position: absolute; display: flex; align-items: center; gap: 8px; }
  .brand-dot { border-radius: 50%; background: var(--brand); flex: none; }
  .brand-name { font-weight: 700; color: var(--brand); letter-spacing: -0.3px; white-space: nowrap; }

  .headline { position: absolute; color: var(--white); font-weight: 700; line-height: 1; text-shadow: 1px 2px 2px rgba(0,0,0,.55); }
  .headline span { display: block; }

  .benefits { position: absolute; list-style: none; color: var(--white); text-shadow: 1px 1px 1px rgba(0,0,0,.5); }
  .benefits li { position: relative; }
  .benefits li::before { content: "✓"; position: absolute; font-weight: 700; }

  .cta {
    position: absolute; display: flex; align-items: center; justify-content: space-between;
    background: linear-gradient(var(--orange-top), var(--orange-bottom));
    border: 1px solid #b84f08; box-shadow: 0 2px 3px rgba(0,0,0,.4);
    color: var(--button-ink); font-weight: 700; text-decoration: none;
  }
  .cta-play { border-radius: 50%; background: var(--play-disc); border: 2px solid #e88a2a; position: relative; flex: none; }
  .cta-play::after {
    content: ""; position: absolute; top: 50%; left: 55%; transform: translate(-50%, -50%);
    border-style: solid; border-color: transparent transparent transparent var(--orange-top);
  }

  /* 728 x 90 */
  .leaderboard { left: 107px; top: 56px; width: 1027px; height: 127px; }
  .leaderboard .photo { left: 790px; top: 0; width: 237px; height: 127px; }
  .leaderboard .brand { left: 14px; top: 50px; gap: 6px; }
  .leaderboard .brand-dot { width: 24px; height: 24px; }
  .leaderboard .brand-name { font-size: 21px; }
  .leaderboard .headline { left: 300px; top: 26px; font-size: 34px; }
  .leaderboard .headline span + span { font-size: 30px; margin-top: 4px; }
  .leaderboard .benefits { left: 522px; top: 6px; font-size: 20px; line-height: 21px; }
  .leaderboard .benefits li { padding-left: 20px; }
  .leaderboard .benefits li::before { left: 0; font-size: 16px; }
  .leaderboard .benefits li.cont::before { content: none; }
  .leaderboard .cta { left: 831px; top: 59px; width: 183px; height: 51px; padding: 0 6px 0 12px; font-size: 21px; }

  /* 160 x 600 */
  .skyscraper { left: 107px; top: 246px; width: 226px; height: 847px; }
  .skyscraper .photo { left: 0; top: 530px; width: 226px; height: 317px; }
  .skyscraper .brand { left: 10px; top: 30px; gap: 6px; }
  .skyscraper .brand-dot { width: 24px; height: 24px; }
  .skyscraper .brand-name { font-size: 21px; }
  .skyscraper .headline { left: 0; width: 226px; top: 163px; font-size: 30px; text-align: center; }
  .skyscraper .headline span + span { margin-top: 2px; }
  .skyscraper .benefits { left: 14px; top: 256px; font-size: 27px; line-height: 31px; }
  .skyscraper .benefits li { padding-left: 28px; }
  .skyscraper .benefits li::before { left: 0; font-size: 22px; }
  .skyscraper .cta { left: 23px; top: 756px; width: 181px; height: 51px; padding: 0 6px 0 12px; font-size: 21px; }

  /* 300 x 250 */
  .rectangle { left: 682px; top: 522px; width: 424px; height: 353px; }
  .rectangle .photo { left: 0; top: 70px; width: 424px; height: 283px; }
  .rectangle .brand { left: 0; width: 424px; justify-content: center; top: 16px; }
  .rectangle .brand-dot { width: 30px; height: 30px; }
  .rectangle .brand-name { font-size: 28px; }
  .rectangle .headline { left: 12px; top: 112px; font-size: 35px; }
  .rectangle .headline span + span { font-size: 29px; margin-top: 2px; }
  .rectangle .benefits { left: 12px; top: 178px; font-size: 20px; line-height: 21px; }
  .rectangle .benefits li { padding-left: 17px; }
  .rectangle .benefits li::before { left: 0; font-size: 16px; }
  .rectangle .benefits li.cont::before { content: none; }
  .rectangle .cta { left: 11px; top: 292px; width: 182px; height: 49px; padding: 0 6px 0 12px; font-size: 21px; }

  .cta-play { width: 38px; height: 38px; }
  .cta-play::after { border-width: 8px 0 8px 12px; }
</style>
</head>
<body>

  <!-- Leaderboard 728x90 -->
  <section class="banner leaderboard" aria-label="728 by 90 banner">
    <div class="photo" role="img" aria-label="Photo of a smiling businesswoman working at a laptop in an office"></div>
    <svg class="shapes" width="1027" height="127" viewBox="0 0 1027 127" aria-hidden="true">
      <defs>
        <linearGradient id="lbMaroon" x1="0" y1="0" x2="0" y2="1">
          <stop offset="0" stop-color="#7a2a40"/><stop offset="1" stop-color="#561a2a"/>
        </linearGradient>
        <linearGradient id="lbSteel" x1="0" y1="0" x2="1" y2="0">
          <stop offset="0" stop-color="#9fb6c9"/><stop offset="1" stop-color="#4e6f8c"/>
        </linearGradient>
      </defs>
      <path d="M255 0 L790 0 L828 63 L790 127 L255 127 Q232 63 255 0 Z" fill="url(#lbMaroon)"/>
      <polyline points="790,0 828,63 790,127" fill="none" stroke="#d8c69c" stroke-width="7"/>
      <path d="M240 0 L262 0 Q240 63 262 127 L240 127 Q216 63 240 0 Z" fill="url(#lbSteel)"/>
    </svg>
    <div class="brand"><span class="brand-dot"></span><span class="brand-name">BrightLedgerHub</span></div>
    <h2 class="headline"><span>CRM FOR</span><span>MORTGAGE</span></h2>
    <ul class="benefits">
      <li>Compliant Platform</li>
      <li>Exclusive Leads</li>
      <li>Automated &amp;</li>
      <li class="cont">Personalized</li>
      <li>Marketing Tools</li>
    </ul>
    <a class="cta" href="https://www.brightledgerhub.example/">Read More <span class="cta-play"></span></a>
  </section>
  <div class="size-label" style="left:520px; top:195px;">728X90</div>

  <!-- Skyscraper 160x600 -->
  <section class="banner skyscraper" aria-label="160 by 600 banner">
    <div class="photo" role="img" aria-label="Photo of a smiling businesswoman working at a laptop in an office"></div>
    <svg class="shapes" width="226" height="847" viewBox="0 0 226 847" aria-hidden="true">
      <defs>
        <linearGradient id="skMaroon" x1="0" y1="0" x2="1" y2="0">
          <stop offset="0" stop-color="#561a2a"/><stop offset=".5" stop-color="#7a2a40"/><stop offset="1" stop-color="#561a2a"/>
        </linearGradient>
        <linearGradient id="skSteel" x1="0" y1="0" x2="0" y2="1">
          <stop offset="0" stop-color="#9fb6c9"/><stop offset="1" stop-color="#4e6f8c"/>
        </linearGradient>
      </defs>
      <path d="M0 537 L113 603 L226 537 V556 L113 622 L0 556 Z" fill="#d8c69c"/>
      <path d="M0 100 H226 V537 L113 603 L0 537 Z" fill="url(#skMaroon)"/>
      <path d="M0 0 H226 V122 Q113 82 0 122 Z" fill="#ffffff"/>
      <path d="M0 122 Q113 82 226 122 V136 Q113 96 0 136 Z" fill="url(#skSteel)"/>
    </svg>
    <div class="brand"><span class="brand-dot"></span><span class="brand-name">BrightLedgerHub</span></div>
    <h2 class="headline"><span>CRM FOR</span><span>MORTGAGE</span></h2>
    <ul class="benefits">
      <li>Compliant<br>Platform</li>
      <li>Exclusive<br>Leads</li>
      <li>Automated &amp;<br>Personalized</li>
      <li>Marketing<br>Tools</li>
    </ul>
    <a class="cta" href="https://www.brightledgerhub.example/">Read More <span class="cta-play"></span></a>
  </section>
  <div class="size-label" style="left:120px; top:1118px;">160X600</div>

  <!-- Medium rectangle 300x250 -->
  <section class="banner rectangle" aria-label="300 by 250 banner">
    <div class="photo" role="img" aria-label="Photo of a smiling businesswoman working at a laptop in an office"></div>
    <svg class="shapes" width="424" height="353" viewBox="0 0 424 353" aria-hidden="true">
      <defs>
        <linearGradient id="reMaroon" x1="0" y1="0" x2="0" y2="1">
          <stop offset="0" stop-color="#7a2a40"/><stop offset="1" stop-color="#561a2a"/>
        </linearGradient>
        <linearGradient id="reSteel" x1="0" y1="0" x2="0" y2="1">
          <stop offset="0" stop-color="#9fb6c9"/><stop offset="1" stop-color="#4e6f8c"/>
        </linearGradient>
      </defs>
      <path d="M0 60 H222 L250 212 L222 353 H0 Z" fill="url(#reMaroon)"/>
      <polyline points="222,70 250,212 222,353" fill="none" stroke="#d8c69c" stroke-width="7"/>
      <path d="M0 0 H424 V94 Q212 50 0 94 Z" fill="#ffffff"/>
      <path d="M0 94 Q212 50 424 94 V107 Q212 63 0 107 Z" fill="url(#reSteel)"/>
    </svg>
    <div class="brand"><span class="brand-dot"></span><span class="brand-name">BrightLedgerHub</span></div>
    <h2 class="headline"><span>CRM FOR</span><span>MORTGAGE</span></h2>
    <ul class="benefits">
      <li>Compliant Platform</li>
      <li>Exclusive Leads</li>
      <li>Automated &amp;</li>
      <li class="cont">Personalized</li>
      <li>Marketing Tools</li>
    </ul>
    <a class="cta" href="https://www.brightledgerhub.example/">Read More <span class="cta-play"></span></a>
  </section>
  <div class="size-label" style="left:794px; top:892px;">300X250</div>

</body>
</html>
```